Virtual Assistant/Online Marketing Business Card/Stationary

I need a professional but modern business card/stationary for my company in Dallas called Brivolo. Brivolo is a virtual assistant specializing in online marketing. I would like a unique design that stands out and makes my brand clear. Incorporating the logo is a must and have attached it to this brief.

Target Market(s)

small business owners & entrepreneurs, 35-65

Industry/Entity Type

Business

Contact Information for Business Card

Maren Tolk
marentolk@brivolo.biz
(555) 271-9064
brivolo.biz

Font styles to use
Sans Serif

Colors
f04a50
3176b5
9bcb3c

Requirements
Must have
• Colors that match the logo colors. Logo integration

```html
<!DOCTYPE html>
<html lang="en">
<head>
<meta charset="utf-8">
<title>Brivolo Business Card</title>
<link href="https://fonts.googleapis.com/css2?family=Montserrat:wght@400;700;800&display=swap" rel="stylesheet">
<style>
  :root {
    --page-bg: #d9d9db;
    --card-dark: #1c1c1e;
    --card-light: #ffffff;
    --ink-dark: #111113;
    --ink-light: #ffffff;
    --accent-red: #f04a50;
    --accent-blue: #3176b5;
    --accent-green: #9bcb3c;
    --accent-cyan: #2bb6d3;
  }
  * { margin: 0; padding: 0; box-sizing: border-box; }
  html, body {
    width: 1200px; height: 960px; overflow: hidden;
    background: var(--page-bg);
    font-family: "Montserrat", sans-serif;
  }
  .sheet {
    width: 1200px; height: 960px;
    display: flex; align-items: center; justify-content: center; gap: 90px;
  }
  .card {
    width: 340px; height: 595px;
    position: relative; overflow: hidden;
    border-radius: 4px;
    box-shadow: 0 14px 30px rgba(0,0,0,.25);
  }
  /* front */
  .card-front { background: var(--card-dark); }
  .front-brand {
    position: absolute; left: 50%; top: 50%;
    transform: translate(-50%, -50%) rotate(-90deg);
    display: flex; align-items: center; gap: 14px;
    white-space: nowrap;
  }
  .brand-name {
    font-weight: 800; font-size: 64px; letter-spacing: -1px;
    color: var(--ink-light);
  }
  .brand-dot {
    width: 22px; height: 22px; border-radius: 50%;
    background: var(--accent-red);
  }
  /* back */
  .card-back { background: var(--card-light); }
  .back-brand {
    position: absolute; left: 0; right: 0; top: 150px;
    display: flex; justify-content: center; align-items: center; gap: 12px;
  }
  .back-brand .brand-name { color: var(--ink-dark); font-size: 58px; }
  .contact-band {
    position: absolute; left: 0; bottom: 0; width: 340px; height: 300px;
  }
  .contact {
    position: absolute; right: 22px; bottom: 70px;
    color: var(--ink-light); text-align: right;
  }
  .contact-name { font-weight: 700; font-size: 21px; margin-bottom: 22px; }
  .contact-line {
    display: flex; justify-content: flex-end; align-items: center; gap: 8px;
    font-size: 14px; line-height: 24px;
  }
  .contact-line svg { width: 13px; height: 13px; flex: none; }
</style>
</head>
<body>
<main class="sheet">
  <section class="card card-front">
    <div class="front-brand">
      <span class="brand-name">Brivolo</span>
      <span class="brand-dot"></span>
    </div>
  </section>

  <section class="card card-back">
    <div class="back-brand">
      <span class="brand-name">Brivolo</span>
      <span class="brand-dot"></span>
    </div>
    <svg class="contact-band" viewBox="0 0 340 300" preserveAspectRatio="none">
      <polygon points="0,110 90,140 340,20 340,300 0,300" fill="var(--card-dark)"/>
    </svg>
    <div class="contact">
      <p class="contact-name">Maren Tolk</p>
      <p class="contact-line">(555) 271-9064
        <svg viewBox="0 0 16 16"><path d="M3 1h3l1 4-2 1a9 9 0 0 0 5 5l1-2 4 1v3a2 2 0 0 1-2 2A13 13 0 0 1 1 3a2 2 0 0 1 2-2z" fill="var(--accent-cyan)"/></svg>
      </p>
      <p class="contact-line">marentolk@brivolo.biz
        <svg viewBox="0 0 16 16"><rect x="1" y="3" width="14" height="10" fill="var(--accent-cyan)"/><path d="M1 3l7 6 7-6" stroke="var(--card-dark)" stroke-width="1.5" fill="none"/></svg>
      </p>
      <p class="contact-line">brivolo.biz
        <svg viewBox="0 0 16 16"><circle cx="8" cy="8" r="6.5" fill="none" stroke="var(--accent-cyan)" stroke-width="1.8"/><path d="M1.5 8h13M8 1.5c-3 3-3 10 0 13M8 1.5c3 3 3 10 0 13" stroke="var(--accent-cyan)" stroke-width="1.3" fill="none"/></svg>
      </p>
    </div>
  </section>
</main>
</body>
</html>
```